依頼詳細
PCとスマホデザインの両方納品をいただきますが、
まずはデザインイメージが確認しやすいPCページのみの提案をお願いします。
PCページはアートボード幅を1366px、コンテンツ幅を1000pxのもので作成してください。
スマホページは当選者に納品時にお願いしたいと思います。
スマホサイズは横幅750pxのサイズで作成してください。

レスポンシブウェブデザインを意識したデザインでお願いします。

デザインに関しては、添付してあるデザインレイアウト設計シートを基にお願いします。
参考サイトのURLはデザインレイアウト設計シートに記載してあります。
画像データについては、フリー素材から流用してイメージ画像に当て込んでください。

足りない場合は、一旦他のサイトの写真をサンプルとして入れてください。(サンプルなどの表記をお願いします)
また、購入が必要な写真などを利用した場合、価格とサイト名を教えてください。
ページ数
1ページ
希望イメージ
シンプル 複雑
単色 カラフル
暗い 明るい
日常 高級
遊び心 厳粛
未来的 伝統的
女性的 男性的
希望する色
緑系
納品ファイル
• イラストレーター形式 (.ai)
• フォトショップ形式 (.psd)
• PNG形式 (.png)
補足説明
上記のいずれか1つ(アウトラインありとなしの2つ)と高解像度JPGを納品お願いします。

```html
<!DOCTYPE html>
<html lang="ja">
<head>
<meta charset="utf-8">
<title>みどり環境サービス</title>
<link href="https://fonts.googleapis.com/css2?family=Noto+Sans+JP:wght@400;500;700;900&display=swap" rel="stylesheet">
<style>
:root{
  --green:#2fb04a;
  --green-dark:#1f8a36;
  --green-pale:#e9f6ec;
  --orange:#f28c1c;
  --red:#e3242b;
  --yellow:#ffe23a;
  --gray-bg:#eeeeee;
  --gray-line:#d8d8d8;
  --text:#333333;
  --muted:#777777;
  --white:#ffffff;
  --gold:#e2b33c;
}
*{box-sizing:border-box;margin:0;padding:0}
html,body{width:1200px;height:5212px;overflow:hidden}
body{font-family:"Noto Sans JP",sans-serif;color:var(--text);background:var(--white);position:relative}
.inner{width:900px;margin:0 auto;position:relative}

/* header */
.site-header{height:128px;display:flex;align-items:center;padding:0 60px;gap:24px}
.logo{width:180px;height:64px;border:2px solid var(--gray-line);display:flex;align-items:center;justify-content:center;font-size:16px;color:var(--green);font-weight:700}
.header-contact{margin-left:auto;display:flex;align-items:center;gap:14px}
.tel-block{display:flex;flex-direction:column;gap:4px}
.pill{background:var(--green);color:var(--white);font-size:12px;font-weight:700;border-radius:20px;padding:4px 16px;display:inline-block}
.tel-small{font-size:11px;color:var(--muted)}
.tel-line{display:flex;align-items:center;gap:8px}
.free-mark{width:34px;height:22px;background:var(--green);border-radius:3px}
.tel-num{font-size:30px;font-weight:700;letter-spacing:1px}
.person-slot{width:60px;height:86px;background:linear-gradient(#f4efe8,#d9cfc4);border-radius:4px}
.btn{display:flex;align-items:center;justify-content:center;gap:6px;color:var(--white);font-weight:700;font-size:13px;border-radius:6px;height:48px;padding:0 14px;text-align:center;line-height:1.3}
.btn-green{background:var(--green)}
.btn-orange{background:var(--orange)}
.btn .dot{width:14px;height:14px;border-radius:50%;background:var(--white);flex:none}

/* nav */
.global-nav{height:104px;background:var(--gray-bg)}
.global-nav ul{list-style:none;display:flex;justify-content:center;gap:8px;padding-top:14px}
.global-nav li{width:160px;height:76px;background:var(--white);border-bottom:6px solid var(--green);display:flex;flex-direction:column;align-items:center;justify-content:center;gap:8px;font-size:13px;font-weight:700}
.global-nav li svg{width:22px;height:22px}

/* hero */
.hero{height:468px;position:relative;overflow:hidden}
.hero-photo{position:absolute;inset:0;background:linear-gradient(110deg,#6f8fa8 0%,#33506a 35%,#1f3d5a 60%,#d9dfe6 82%,#f2f2f2 100%)}
.hero-copy{position:absolute;left:50px;top:40px}
.hero-line{display:inline-block;font-size:50px;font-weight:900;color:var(--white);text-shadow:0 0 6px #000,0 0 2px #000;line-height:1.25}
.hero-band{display:inline-block;margin-top:14px;background:rgba(255,255,255,.92);font-size:40px;font-weight:900;padding:2px 12px}
.hero-band em{font-style:normal;color:var(--green)}
.hero-catch{display:block;margin-top:18px;font-size:74px;font-weight:900;color:var(--yellow);text-shadow:0 0 8px #000,0 0 3px #000;letter-spacing:2px}

/* section headings */
.sec-title{text-align:center;font-size:26px;font-weight:700}
.sec-title .box{display:inline-block;background:var(--green);color:var(--white);width:42px;height:42px;line-height:42px;margin-right:2px;text-align:center}

/* promises */
.promises{height:700px;padding-top:48px}
.promise-grid{display:grid;grid-template-columns:repeat(3,270px);gap:40px 45px;margin-top:48px}
.promise-card{text-align:center}
.promise-img{height:130px;border-radius:2px}
.num{width:44px;height:44px;border-radius:50%;background:var(--orange);color:var(--white);font-weight:700;font-size:20px;line-height:44px;margin:-22px auto 6px;position:relative}
.promise-card h3{font-size:19px;font-weight:700;margin-bottom:8px}
.promise-card p{font-size:12px;color:var(--muted);line-height:1.7}

/* cta */
.cta{height:420px;padding-top:20px}
.cta-box{width:800px;margin:0 auto;border:4px solid var(--green);border-radius:6px;padding:30px 40px;position:relative;background:var(--white);box-shadow:0 3px 8px rgba(0,0,0,.12)}
.cta-box h2{text-align:center;font-size:34px;font-weight:900}
.cta-box h2 .free{color:var(--red);margin-left:10px}
.cta-lead{text-align:center;font-size:15px;line-height:1.8;margin-top:8px}
.cta-body{margin-top:16px;padding-left:20px}
.cta-body .tel-num{font-size:40px}
.cta-buttons{display:flex;gap:12px;margin-top:16px;width:530px}
.cta-buttons .btn{flex:1;height:54px}
.cta-person{position:absolute;right:50px;top:150px;width:150px;height:170px;background:linear-gradient(#f5f0ea,#d7cdc2);border-radius:4px}

/* services */
.services{height:980px;background:var(--gray-bg);padding-top:160px}
.service-grid{display:grid;grid-template-columns:repeat(3,270px);gap:50px 45px;margin-top:60px}
.service-item{height:186px;position:relative;border-radius:2px}
.service-item span{position:absolute;left:0;bottom:18px;background:var(--green);color:var(--white);font-size:13px;font-weight:700;padding:6px 16px}

/* results */
.results{height:960px;padding-top:100px;text-align:center}
.medal{width:64px;height:64px;border-radius:50%;background:radial-gradient(#f7d66b,var(--gold));margin:0 auto}
.results h2{font-size:20px;font-weight:700;margin-top:12px}
.results .count{font-size:26px;font-weight:700;margin-top:18px}
.results .count strong{color:var(--red);font-size:48px}
.results p.desc{font-size:15px;line-height:1.8;margin-top:6px}
.awards{display:flex;justify-content:center;gap:90px;margin-top:60px}
.award h3{font-size:14px;font-weight:500;line-height:1.6}
.trophy{width:200px;height:180px;margin-top:16px;background:radial-gradient(circle at 50% 40%,#f7d66b,#e2b33c 55%,transparent 70%)}
.banners{display:flex;justify-content:center;gap:40px;margin-top:56px}
.banner{width:430px;height:140px;position:relative;border-radius:2px}
.banner span{position:absolute;background:var(--green);color:var(--white);font-weight:700;font-size:22px;padding:6px 18px}

/* news */
.news{height:480px;background:var(--gray-bg);padding-top:100px}
.news-list{list-style:none;margin-top:56px;background:var(--white)}
.news-list li{display:flex;gap:40px;padding:22px 30px;border-bottom:1px solid var(--gray-line);font-size:14px}
.news-list time{font-weight:700;width:140px}
.news-list .new{color:var(--red);font-size:12px;margin-left:8px}
.more{display:block;width:200px;margin:26px auto 0;background:var(--green);color:var(--white);text-align:center;font-size:14px;font-weight:700;padding:12px 0;border-radius:4px}

/* cta2 */
.cta.cta-bottom{height:480px;padding-top:80px}

/* footer */
.site-footer{height:492px;background:var(--gray-bg);position:relative;padding-top:60px}
.footer-inner{display:flex;gap:60px}
.footer-info{width:380px;font-size:13px;line-height:1.9}
.footer-info .logo{margin-bottom:26px}
.footer-info .tel-num{font-size:32px}
.footer-links{display:flex;gap:50px;font-size:13px}
.footer-links ul{list-style:none;line-height:2.2}
.footer-links li::before{content:"› ";color:var(--green);font-weight:700}
.social{display:flex;gap:14px;margin-top:24px}
.social span{width:30px;height:30px;border-radius:50%;background:var(--green)}
.copyright{position:absolute;left:0;right:0;bottom:0;height:44px;background:var(--green-dark);color:var(--white);font-size:11px;text-align:center;line-height:44px}
</style>
</head>
<body>

<header class="site-header">
  <div class="logo">みどり環境サービス</div>
  <div class="header-contact">
    <div class="tel-block">
      <span class="pill">お気軽にお電話ください。</span>
      <span class="tel-small">フリーダイヤル</span>
      <div class="tel-line"><span class="free-mark"></span><span class="tel-num">0120-000-123</span></div>
    </div>
    <div class="person-slot" role="img" aria-label="ヘッドセットを付けた受付スタッフの写真"></div>
    <a class="btn btn-green"><span class="dot"></span>チャットで相談</a>
    <a class="btn btn-orange">インターネットから<br>簡単お見積り</a>
    <a class="btn btn-green"><span class="dot"></span>お問い合わせ</a>
  </div>
</header>

<nav class="global-nav">
  <ul>
    <li><svg viewBox="0 0 24 24"><path d="M3 11 12 3l9 8v10h-6v-6H9v6H3z" fill="#2fb04a"/></svg>ホーム</li>
    <li><svg viewBox="0 0 24 24"><rect x="3" y="4" width="18" height="4" fill="#2fb04a"/><rect x="3" y="10" width="18" height="4" fill="#2fb04a"/><rect x="3" y="16" width="18" height="4" fill="#2fb04a"/></svg>サービス一覧</li>
    <li><svg viewBox="0 0 24 24"><circle cx="12" cy="12" r="10" fill="#2fb04a"/><text x="12" y="17" font-size="14" fill="#fff" text-anchor="middle" font-weight="700">?</text></svg>よくある質問</li>
    <li><svg viewBox="0 0 24 24"><circle cx="12" cy="10" r="7" fill="#2fb04a"/><path d="M8 16l-2 6 6-3 6 3-2-6z" fill="#2fb04a"/></svg>作業実績</li>
    <li><svg viewBox="0 0 24 24"><rect x="4" y="3" width="16" height="18" fill="#2fb04a"/><rect x="7" y="6" width="4" height="3" fill="#fff"/><rect x="13" y="6" width="4" height="3" fill="#fff"/><rect x="7" y="11" width="4" height="3" fill="#fff"/><rect x="13" y="11" width="4" height="3" fill="#fff"/></svg>会社案内</li>
  </ul>
</nav>

<section class="hero">
  <div class="hero-photo" role="img" aria-label="浄化槽清掃用の青いバキュームカーと受付スタッフの写真"></div>
  <div class="hero-copy">
    <span class="hero-line">浄化槽の点検・清掃</span><br>
    <span class="hero-line">迅速な対応が可能です!</span><br>
    <span class="hero-band"><em>みどり環境</em>にお任せください!</span>
    <span class="hero-catch">速い!安い!確実!</span>
  </div>
</section>

<section class="promises">
  <div class="inner">
    <h2 class="sec-title"><span class="box">安</span><span class="box">心</span>してご利用いただける6つのお約束</h2>
    <div class="promise-grid">
      <div class="promise-card"><div class="promise-img" role="img" aria-label="作業道具の写真" style="background:linear-gradient(#c9c2b6,#8d8577)"></div><div class="num">1</div><h3>充実のサポート</h3><p>小さなことでもお気軽にご相談下さい。<br>丁寧にしっかり対応いたします。</p></div>
      <div class="promise-card"><div class="promise-img" role="img" aria-label="自宅で電話する女性の写真" style="background:linear-gradient(#dbe3ea,#a9b7c4)"></div><div class="num">2</div><h3>自宅にいるだけでOK</h3><p>ご指定の場所までお伺いし<br>作業は全てスタッフにお任せください。</p></div>
      <div class="promise-card"><div class="promise-img" role="img" aria-label="スタッフ三人の写真" style="background:linear-gradient(#e7ecf2,#8aa0ba)"></div><div class="num">3</div><h3>配慮を忘れません</h3><p>お客様のご近所にも配慮しながら<br>丁寧に作業を進めます。</p></div>
      <div class="promise-card"><div class="promise-img" role="img" aria-label="片付いた室内の写真" style="background:linear-gradient(#f1efe9,#c8c4b8)"></div><div class="num">4</div><h3>信頼できるプロの技術</h3><p>作業実績の豊富なスタッフが<br>一件ずつ確実に対応します。</p></div>
      <div class="promise-card"><div class="promise-img" role="img" aria-label="握手するビジネスマンの写真" style="background:linear-gradient(#5e6d80,#2f3a48)"></div><div class="num">5</div><h3>安心保証サービス</h3><p>作業後のトラブルにも<br>責任を持って対応いたします。</p></div>
      <div class="promise-card"><div class="promise-img" role="img" aria-label="時計と書類の写真" style="background:linear-gradient(#eeeeea,#c7c7bf)"></div><div class="num">6</div><h3>お急ぎの方も大歓迎</h3><p>ご依頼当日のご対応も<br>可能な限り迅速に承ります。</p></div>
    </div>
  </div>
</section>

<section class="cta">
  <div class="cta-box">
    <h2>お見積り ご相談<span class="free">無料!</span></h2>
    <p class="cta-lead">浄化槽のことや不用品回収・産廃物の処理など<br>お客様のお困りごとに対して柔軟に対応いたします。</p>
    <div class="cta-body">
      <span class="pill">お気軽にご相談ください。</span>
      <div class="tel-small" style="margin-top:8px">フリーダイヤル</div>
      <div class="tel-line"><span class="free-mark"></span><span class="tel-num">0120-000-123</span></div>
      <div class="cta-buttons">
        <a class="btn btn-green"><span class="dot"></span>チャットで相談</a>
        <a class="btn btn-orange">インターネットから<br>簡単お見積り</a>
        <a class="btn btn-green"><span class="dot"></span>お問い合わせ</a>
      </div>
    </div>
    <div class="cta-person" role="img" aria-label="受付スタッフの写真"></div>
  </div>
</section>

<section class="services">
  <div class="inner">
    <h2 class="sec-title"><span class="box">サ</span><span class="box">ー</span><span class="box">ビ</span><span class="box">ス</span>のご紹介</h2>
    <div class="service-grid">
      <div class="service-item" role="img" aria-label="浄化槽清掃の作業写真" style="background:linear-gradient(#7c8a6e,#4e5a44)"><span>浄化槽清掃</span></div>
      <div class="service-item" role="img" aria-label="遺品整理の写真" style="background:linear-gradient(#a39480,#6a5c4a)"><span>遺品整理</span></div>
      <div class="service-item" role="img" aria-label="段ボールが積まれた部屋の写真" style="background:linear-gradient(#c7a57a,#8a6a44)"><span>丸ごとおかたづけ</span></div>
      <div class="service-item" role="img" aria-label="不用品回収の写真" style="background:linear-gradient(#8ea4b8,#53677a)"><span>不用品回収</span></div>
      <div class="service-item" role="img" aria-label="産業廃棄物の写真" style="background:linear-gradient(#777,#3d3d3d)"><span>産廃物処理</span></div>
      <div class="service-item" role="img" aria-label="電話対応する女性の写真" style="background:linear-gradient(#f0e6dc,#c6b09c)"><span>その他サービス</span></div>
      <div class="service-item" role="img" aria-label="清掃作業の写真" style="background:linear-gradient(#b9c4cc,#6f7d88)"><span>すっきりハウス清掃</span></div>
    </div>
  </div>
</section>

<section class="results">
  <div class="medal" role="img" aria-label="メダルのアイコン"></div>
  <h2>作業実績</h2>
  <p class="count">年間作業実績<strong>23,449</strong>件!</p>
  <p class="desc">みどり環境では、年間23,449件の作業実績がございます。<br>不用品回収はもちろん、不用品買取・遺品整理・生前整理など、<br>お客様のお困りごとを解決いたします。</p>
  <div class="awards">
    <div class="award"><h3>不用品回収サービス<br>口コミ満足度</h3><div class="trophy" role="img" aria-label="第一位のトロフィー"></div></div>
    <div class="award"><h3>不用品回収サービス<br>スタッフ対応満足度</h3><div class="trophy" role="img" aria-label="第一位のトロフィー"></div></div>
    <div class="award"><h3>不用品回収サービス<br>価格満足度</h3><div class="trophy" role="img" aria-label="第一位のトロフィー"></div></div>
  </div>
  <div class="banners">
    <div class="banner" role="img" aria-label="作業車両の写真" style="background:linear-gradient(90deg,#3b4650,#8896a2)"><span style="left:30px;top:40px">会社案内</span></div>
    <div class="banner" role="img" aria-label="スタッフの写真" style="background:linear-gradient(90deg,#dfe5ea,#8ea0b2)"><span style="right:30px;top:40px">採用情報</span></div>
  </div>
</section>

<section class="news">
  <div class="inner">
    <h2 class="sec-title"><span class="box">新</span><span class="box">着</span><span class="box">情</span><span class="box">報</span></h2>
    <ul class="news-list">
      <li><time>2021.09.08<span class="new">NEW</span></time>ここにタイトルが入ります。ここにタイトルが入ります。ここにタイトルが入ります。</li>
      <li><time>2021.08.07</time>ここにタイトルが入ります。ここにタイトルが入ります。ここにタイトルが入ります。</li>
      <li><time>2021.08.06</time>ここにタイトルが入ります。ここにタイトルが入ります。ここにタイトルが入ります。</li>
    </ul>
    <a class="more">一覧を見る ›</a>
  </div>
</section>

<section class="cta cta-bottom">
  <div class="cta-box">
    <h2>お見積り ご相談<span class="free">無料!</span></h2>
    <p class="cta-lead">浄化槽のことや不用品回収・産廃物の処理など<br>お客様のお困りごとに対して柔軟に対応いたします。</p>
    <div class="cta-body">
      <span class="pill">お気軽にご相談ください。</span>
      <div class="tel-small" style="margin-top:8px">フリーダイヤル</div>
      <div class="tel-line"><span class="free-mark"></span><span class="tel-num">0120-000-123</span></div>
      <div class="cta-buttons">
        <a class="btn btn-green"><span class="dot"></span>チャットで相談</a>
        <a class="btn btn-orange">インターネットから<br>簡単お見積り</a>
        <a class="btn btn-green"><span class="dot"></span>お問い合わせ</a>
      </div>
    </div>
    <div class="cta-person" role="img" aria-label="受付スタッフの写真"></div>
  </div>
</section>

<footer class="site-footer">
  <div class="inner footer-inner">
    <div class="footer-info">
      <div class="logo">みどり環境サービス</div>
      <p>〒000-0000 緑ヶ丘市中央町1丁目2番3号</p>
      <div class="tel-small">フリーダイヤル</div>
      <div class="tel-line"><span class="free-mark"></span><span class="tel-num">0120-000-123</span></div>
      <p>TEL：0000-12-3456　FAX：0000-12-3457</p>
      <p>e-mail：info@midori-kankyo.example</p>
    </div>
    <div>
      <div class="footer-links">
        <ul><li>サービス一覧</li><li>浄化槽清掃</li><li>丸ごとおかたづけ</li><li>不用品回収</li><li>産廃物処理</li><li>遺品整理</li><li>すっきりハウス清掃</li><li>その他サービス</li></ul>
        <ul><li>よくある質問</li><li>作業実績</li><li>会社案内</li><li>採用情報</li></ul>
        <ul><li>個人情報保護方針</li><li>お問い合わせ</li></ul>
      </div>
      <div class="social"><span></span><span></span><span></span></div>
    </div>
  </div>
  <div class="copyright">Copyright © みどり環境サービス All Rights Reserved.</div>
</footer>

</body>
</html>
```